Industrial Services company needs a business card design

We provide industrial maintenance services including sandblasting, painting, pressure washing, storage tank rehabilitation, and welding. I would like an industrial design that's eye catching. I would like the back-side of the card to list our services.

Industry/Entity Type

Construction

Contact Information for Business Card

address: 418 Hartwell Lane, York, PA 17405
Phone: 410-637-4815
email: corvethinc@mailbrook.net
Daniel Verhoeven, President
www.corvethcoating.net

Logo Text

Corveth Industrial Services

Font styles to use
Sans Serif

Colors
000000
229ed3
0692cd
ffffff

Requirements
Must have
• Easy to read
• our services listed/included on back of card
• eye catching color combinations
Nice to have
• Water storage tank image

```html
<!DOCTYPE html>
<html lang="en">
<head>
<meta charset="utf-8">
<title>Corveth Industrial Services – Business Card</title>
<link rel="stylesheet" href="https://fonts.googleapis.com/css2?family=Montserrat:ital,wght@0,400;0,500;0,600;0,700;1,500;1,600&display=swap">
<style>
  :root {
    --brand-blue: #3194cc;
    --ink: #000000;
    --card-black: #070909;
    --paper: #ffffff;
    --trim: #1a1a1a;
    --faint: #e9ecef;
    --table: #d9dbde;
  }
  * { margin: 0; padding: 0; box-sizing: border-box; }
  html, body { width: 849px; height: 1200px; overflow: hidden; background: var(--paper); }
  body { position: relative; font-family: "Montserrat", sans-serif; color: var(--ink); }

  .top-band { position: absolute; left: 0; top: 0; width: 849px; height: 51px; background: var(--brand-blue); }
  .black-band { position: absolute; left: 0; top: 51px; width: 849px; height: 26px; background: var(--ink); }

  .brand-mark { position: absolute; left: 354px; top: 146px; width: 140px; height: 140px; border-radius: 50%; background: var(--brand-blue); }
  .brand-name { position: absolute; left: 0; top: 303px; width: 849px; text-align: center; font-size: 17px; font-weight: 600; color: var(--brand-blue); }

  .palette-line { position: absolute; top: 389px; height: 3px; }
  .palette-line.black { left: 0; width: 362px; background: var(--ink); }
  .palette-line.blue { left: 477px; width: 372px; background: var(--brand-blue); }
  .swatch { position: absolute; top: 369px; width: 44px; height: 43px; }
  .swatch.black { left: 362px; background: var(--ink); }
  .swatch.blue { left: 433px; background: var(--brand-blue); }
  .swatch-label { position: absolute; top: 415px; width: 60px; text-align: center; font-size: 11px; font-weight: 600; }
  .swatch-label.black { left: 354px; color: var(--ink); }
  .swatch-label.blue { left: 425px; color: var(--brand-blue); }

  .section-label { position: absolute; left: 53px; font-size: 11px; font-weight: 600; color: var(--ink); }
  .section-label.print { top: 446px; }
  .section-label.mock { left: 68px; top: 795px; }

  .trim-marks { position: absolute; left: 0; top: 470px; width: 849px; height: 330px; }

  /* card artwork */
  .card { position: absolute; left: 0; top: 0; width: 392px; height: 245px; overflow: hidden; }
  .card-front { background: var(--card-black); }
  .card-front .front-mark { position: absolute; left: 151px; top: 60px; width: 90px; height: 90px; border-radius: 50%; background: var(--brand-blue); }
  .card-front .front-name { position: absolute; left: 0; top: 166px; width: 392px; text-align: center; font-size: 15px; font-weight: 600; color: var(--brand-blue); }

  .card-back { background: var(--paper); }
  .card-back .faint-mark { position: absolute; left: 230px; top: 60px; width: 130px; height: 130px; border-radius: 50%; background: var(--faint); opacity: .7; }
  .holder-name { position: absolute; left: 35px; top: 86px; font-size: 14.5px; font-weight: 700; color: var(--brand-blue); line-height: 1.3; letter-spacing: .1px; }
  .holder-name .role { display: block; font-weight: 600; }
  .contact { position: absolute; left: 35px; top: 129px; font-size: 6.6px; font-weight: 500; color: var(--brand-blue); line-height: 9.8px; }
  .contact dt { float: left; clear: left; width: 34px; }
  .contact dd { margin-left: 34px; }
  .divider { position: absolute; left: 201px; top: 69px; width: 2px; height: 115px; background: var(--brand-blue); }
  .services { position: absolute; left: 225px; top: 79px; color: var(--brand-blue); }
  .services h3 { font-size: 10.5px; font-weight: 600; font-style: italic; letter-spacing: 1px; text-decoration: underline; margin-bottom: 7px; }
  .services ul { list-style: none; }
  .services li { font-size: 9.4px; font-weight: 600; font-style: italic; line-height: 13.7px; position: relative; padding-left: 10px; }
  .services li::before { content: ""; position: absolute; left: 0; top: 5px; width: 4px; height: 4px; background: var(--brand-blue); }

  /* print layout placement */
  .print-slot { position: absolute; top: 512px; width: 392px; height: 245px; }
  .print-slot.front { left: 17px; }
  .print-slot.back { left: 440px; }

  /* flat card sample sheet */
  .sample-sheet { position: absolute; left: 2px; top: 818px; width: 847px; height: 382px; background: var(--table); }
  .sample-slot { position: absolute; width: 180px; height: 112.5px; overflow: hidden; box-shadow: 0 3px 8px rgba(0,0,0,.25); }
  .sample-slot .card { transform: scale(0.4592); transform-origin: 0 0; }
  .sample-slot.c1 { left: 24px; } .sample-slot.c2 { left: 230px; }
  .sample-slot.c3 { left: 436px; } .sample-slot.c4 { left: 642px; }
  .sample-slot.r1 { top: 63px; } .sample-slot.r2 { top: 206px; }
</style>
</head>
<body>
  <div class="top-band"></div>
  <div class="black-band"></div>

  <div class="brand-mark" aria-hidden="true"></div>
  <h1 class="brand-name">Corveth Industrial Services</h1>

  <div class="palette-line black"></div>
  <div class="palette-line blue"></div>
  <div class="swatch black"></div>
  <div class="swatch blue"></div>
  <div class="swatch-label black">#000000</div>
  <div class="swatch-label blue">#3194cc</div>

  <p class="section-label print">Print Ready Files With a trim lines.</p>

  <svg class="trim-marks" viewBox="0 470 849 330" aria-hidden="true">
    <g stroke="var(--trim)" stroke-width="1" fill="none">
      <path d="M41 475 V512 M0 512 H17 M17 512 V470"/>
      <path d="M385 475 V512 M409 512 H426 M409 512 V500"/>
      <path d="M41 795 V757 M0 757 H17 M17 757 V770"/>
      <path d="M385 795 V757 M409 757 H426 M409 757 V770"/>
      <path d="M464 475 V512 M428 512 H440 M440 500 V530"/>
      <path d="M810 500 H849 M834 500 V535"/>
      <path d="M464 795 V757 M428 757 H440 M440 745 V770"/>
      <path d="M810 757 H849 M834 740 V770"/>
    </g>
  </svg>

  <div class="print-slot front">
    <section class="card card-front">
      <div class="front-mark" aria-hidden="true"></div>
      <p class="front-name">Corveth Industrial Services</p>
    </section>
  </div>

  <div class="print-slot back">
    <section class="card card-back">
      <div class="faint-mark" aria-hidden="true"></div>
      <h2 class="holder-name">DANIEL VERHOEVEN<span class="role">President</span></h2>
      <dl class="contact">
        <dt>Address</dt><dd>: 418 Hartwell Lane, York, PA 17405</dd>
        <dt>Phone</dt><dd>: 410-637-4815</dd>
        <dt>email</dt><dd>: corvethinc@mailbrook.net</dd>
      </dl>
      <div class="divider"></div>
      <div class="services">
        <h3>SERVICES :</h3>
        <ul>
          <li>sandblasting</li>
          <li>painting</li>
          <li>pressure washing</li>
          <li>storage tank rehabilitation</li>
          <li>welding</li>
        </ul>
      </div>
    </section>
  </div>

  <p class="section-label mock">Business Card Mock sample</p>
  <div class="sample-sheet" aria-label="Business card samples, front and back">
    <div class="sample-slot r1 c1"><section class="card card-back"><div class="faint-mark"></div><h2 class="holder-name">DANIEL VERHOEVEN<span class="role">President</span></h2><dl class="contact"><dt>Address</dt><dd>: 418 Hartwell Lane, York, PA 17405</dd><dt>Phone</dt><dd>: 410-637-4815</dd><dt>email</dt><dd>: corvethinc@mailbrook.net</dd></dl><div class="divider"></div><div class="services"><h3>SERVICES :</h3><ul><li>sandblasting</li><li>painting</li><li>pressure washing</li><li>storage tank rehabilitation</li><li>welding</li></ul></div></section></div>
    <div class="sample-slot r1 c2"><section class="card card-front"><div class="front-mark"></div><p class="front-name">Corveth Industrial Services</p></section></div>
    <div class="sample-slot r1 c3"><section class="card card-back"><div class="faint-mark"></div><h2 class="holder-name">DANIEL VERHOEVEN<span class="role">President</span></h2><dl class="contact"><dt>Address</dt><dd>: 418 Hartwell Lane, York, PA 17405</dd><dt>Phone</dt><dd>: 410-637-4815</dd><dt>email</dt><dd>: corvethinc@mailbrook.net</dd></dl><div class="divider"></div><div class="services"><h3>SERVICES :</h3><ul><li>sandblasting</li><li>painting</li><li>pressure washing</li><li>storage tank rehabilitation</li><li>welding</li></ul></div></section></div>
    <div class="sample-slot r1 c4"><section class="card card-front"><div class="front-mark"></div><p class="front-name">Corveth Industrial Services</p></section></div>
    <div class="sample-slot r2 c1"><section class="card card-front"><div class="front-mark"></div><p class="front-name">Corveth Industrial Services</p></section></div>
    <div class="sample-slot r2 c2"><section class="card card-back"><div class="faint-mark"></div><h2 class="holder-name">DANIEL VERHOEVEN<span class="role">President</span></h2><dl class="contact"><dt>Address</dt><dd>: 418 Hartwell Lane, York, PA 17405</dd><dt>Phone</dt><dd>: 410-637-4815</dd><dt>email</dt><dd>: corvethinc@mailbrook.net</dd></dl><div class="divider"></div><div class="services"><h3>SERVICES :</h3><ul><li>sandblasting</li><li>painting</li><li>pressure washing</li><li>storage tank rehabilitation</li><li>welding</li></ul></div></section></div>
    <div class="sample-slot r2 c3"><section class="card card-front"><div class="front-mark"></div><p class="front-name">Corveth Industrial Services</p></section></div>
    <div class="sample-slot r2 c4"><section class="card card-back"><div class="faint-mark"></div><h2 class="holder-name">DANIEL VERHOEVEN<span class="role">President</span></h2><dl class="contact"><dt>Address</dt><dd>: 418 Hartwell Lane, York, PA 17405</dd><dt>Phone</dt><dd>: 410-637-4815</dd><dt>email</dt><dd>: corvethinc@mailbrook.net</dd></dl><div class="divider"></div><div class="services"><h3>SERVICES :</h3><ul><li>sandblasting</li><li>painting</li><li>pressure washing</li><li>storage tank rehabilitation</li><li>welding</li></ul></div></section></div>
  </div>
</body>
</html>
```